Fresh & Clean *NEW* BUSINESS CARD Needed - OPTOMETRY Clinic/Optical

High-tech optometry practice with 3 doctors seeking new business card.  We provide eye exams, sell, designer glasses/contacts/specialty eyewear and treat ocular diseases.  For our business cards, we are seeking fresh, clean, and crisp design as we grow our team (staffing change).  Simply adding doctors is making the card look busy/cluttered.
 Looking for professional, less cluttered look yet still have our logo, doctor names, phone, address, and website....If possible!  :)
Names:
Marisol Pettigrew, O.D.
Ray Bellamy, O.D.
Nora Vantreese, O.D.
Phone: 555-214-6038
Website: www.BrightLensStudio.example
Address:  418 Harlan P. Moody, Larkfield, OK 70000
Ultimately we have the main business card with all doctor sames and that card has two versions  (front is always the same).  The back has two designs (1) displays next appointment time/date, (2) for "general use" (non-appointment.)    I have attached what we have used in the past.  
We also need a design template for each team member in our practice with their name, title, and email.   Those should be designed with the "general use" back (see attached).
**Open to entirely new design so don't feel obligated to keep current format.  Need new perspective!  Also including our watermark and some other design features we have consistently used in past in our portfolio.  Included are two options for logos--vertical and horizontal.
**I also would like to remove "Member of Optic Guild" on our logo if possible**
 Other image files available upon request.

Target Market(s)

New patient & Current Patients

Industry/Entity Type

Optometry

Contact Information for Business Card

High-tech optometry practice with 3 doctors seeking new business card.  We provide eye exams, sell, designer glasses/contacts/specialty eyewear and treat ocular diseases.  For our business cards, we are seeking fresh, clean, and crisp design as we grow our team (staffing change).  Simply adding doctors is making the card look busy/cluttered.  Looking for professional, less cluttered look yet still have our logo, doctor names, phone, address, and website....If possible!  :) Names: Marisol Pettigrew, O.D. Ray Bellamy, O.D. Nora Vantreese, O.D. Phone: 555-214-6038 Website: www.BrightLensStudio.example Address:  418 Harlan P. Moody, Larkfield, OK 70000 Ultimately we have the main business card with all doctor sames and that card has two versions  (front is always the same).  The back has two designs (1) displays next appointment time/date, (2) for "general use" (non-appointment.)    I have attached what we have used in the past.   We also need a design template for each team member in our practice with their name, title, and email.   Those should be designed with the "general use" back (see attached). **Open to entirely new design so don't feel obligated to keep current format.  Need new perspective!  Also including our watermark and some other design features we have consistently used in past in our portfolio.  Included are two options for logos--vertical and horizontal. **I also would like to remove "Member of Optic Guild" on our logo if possible**  Other image files available upon request.

Font styles to use
Other font styles liked:
• We have used Montserrat / Yellowtail in the past

Colors

Designer to choose colors to be used in the design.

Requirements
Must have
• Clean & Fresh Design with Logo / Info provided in description. Horizontal orientation. **I have included the CMYK colors we currently have in our logo.
Should not have
• Cluttered

```html
<!DOCTYPE html>
<html lang="en">
<head>
<meta charset="utf-8">
<title>Bright Lens Studio – Business Cards</title>
<link rel="stylesheet" href="https://fonts.googleapis.com/css2?family=Montserrat:wght@400;500;600;700&display=swap">
<style>
  :root {
    --bg: #2a2c2f;
    --paper: #ffffff;
    --gold: #dfb505;
    --slate: #587483;
    --ink: #5a6066;
    --aqua: #8fd3e0;
    --muted: #7b8085;
    --rule: #9a9ea3;
  }
  * { box-sizing: border-box; margin: 0; padding: 0; }
  html, body { width: 1200px; height: 952px; overflow: hidden; }
  body {
    background: var(--bg);
    font-family: "Montserrat", Arial, sans-serif;
    display: flex;
    flex-direction: column;
    align-items: center;
    justify-content: center;
    gap: 56px;
  }
  .card {
    position: relative;
    width: 600px;
    height: 343px;
    background: var(--paper);
    overflow: hidden;
    box-shadow: 0 10px 26px rgba(0,0,0,.45);
  }
  .brand {
    position: absolute;
    display: flex;
    align-items: center;
    gap: 10px;
    color: var(--ink);
    font-weight: 500;
    letter-spacing: .5px;
    white-space: nowrap;
  }
  .brand-dot {
    width: 30px; height: 30px;
    border-radius: 50%;
    background: var(--aqua);
    flex: none;
  }

  /* Front */
  .front .brand { top: 38px; left: 0; right: 0; justify-content: center; font-size: 30px; }
  .doctors {
    position: absolute;
    top: 128px; left: 30px; right: 30px;
    display: flex;
  }
  .doctor {
    flex: 1;
    text-align: center;
    color: var(--slate);
    position: relative;
    white-space: nowrap;
  }
  .doctor + .doctor::before {
    content: "";
    position: absolute;
    left: 0; top: -6px;
    width: 1px; height: 62px;
    background: linear-gradient(to bottom, rgba(0,0,0,0), rgba(0,0,0,.1), rgba(0,0,0,0));
  }
  .doctor-name { font-size: 18px; font-weight: 600; }
  .doctor-title { font-size: 11px; font-weight: 600; margin-top: 2px; }
  .doctor:nth-child(1) { margin-top: -14px; }
  .doctor:nth-child(3) { margin-top: 14px; }

  .band-contact {
    position: absolute;
    left: 0; right: 0; bottom: 82px;
    height: 40px;
    background: var(--gold);
    display: flex;
    align-items: center;
    gap: 40px;
    padding-left: 56px;
    color: var(--paper);
    font-size: 14px;
    font-weight: 500;
  }
  .contact-item { display: flex; align-items: center; gap: 10px; white-space: nowrap; }
  .contact-icon {
    width: 20px; height: 20px;
    background: var(--slate);
    border-radius: 3px;
    display: flex; align-items: center; justify-content: center;
  }
  .band-address {
    position: absolute;
    left: 0; right: 0; bottom: 28px;
    height: 54px;
    background: var(--slate);
    color: var(--paper);
    font-size: 15px;
    font-weight: 500;
    display: flex;
    align-items: center;
    padding-left: 56px;
    white-space: nowrap;
  }

  /* Back */
  .back .brand { top: 46px; left: 0; right: 0; justify-content: center; font-size: 30px; }
  .band-appointment {
    position: absolute;
    left: 0; right: 0; top: 136px;
    height: 40px;
    background: var(--gold);
    color: var(--paper);
    font-size: 15px;
    font-weight: 700;
    letter-spacing: 1.5px;
    display: flex;
    align-items: center;
    justify-content: flex-end;
    padding-right: 150px;
  }
  .appointment-fields {
    position: absolute;
    left: 40px; right: 40px; top: 238px;
    display: flex;
    gap: 40px;
  }
  .field {
    flex: 1;
    display: flex;
    align-items: flex-end;
    gap: 4px;
    font-size: 12px;
    color: var(--muted);
  }
  .field-line { flex: 1; border-bottom: 1.5px dashed var(--rule); height: 12px; }
</style>
</head>
<body>

  <section class="card front" aria-label="Business card front">
    <div class="brand"><span class="brand-dot"></span>Bright Lens Studio</div>
    <div class="doctors">
      <div class="doctor"><div class="doctor-name">Marisol Pettigrew</div><div class="doctor-title">O.D.</div></div>
      <div class="doctor"><div class="doctor-name">Ray Bellamy</div><div class="doctor-title">O.D.</div></div>
      <div class="doctor"><div class="doctor-name">Nora Vantreese</div><div class="doctor-title">O.D.</div></div>
    </div>
    <div class="band-contact">
      <div class="contact-item">
        <span class="contact-icon">
          <svg width="12" height="12" viewBox="0 0 24 24"><path fill="#fff" d="M6.6 10.8a15 15 0 0 0 6.6 6.6l2.2-2.2a1 1 0 0 1 1-.25 11.4 11.4 0 0 0 3.6.57 1 1 0 0 1 1 1V20a1 1 0 0 1-1 1A17 17 0 0 1 3 4a1 1 0 0 1 1-1h3.5a1 1 0 0 1 1 1c0 1.250.2 2.450.57 3.570a1 1 0 0 1-.25 1z"/></svg>
        </span>555-214-6038
      </div>
      <div class="contact-item">
        <span class="contact-icon">
          <svg width="12" height="12" viewBox="0 0 24 24" fill="none" stroke="#fff" stroke-width="2"><circle cx="12" cy="12" r="9"/><path d="M3 12h18M12 3c3 3 3 15 0 18M12 3c-3 3-3 15 0 18"/></svg>
        </span>www.BrightLensStudio.example
      </div>
    </div>
    <div class="band-address">418 Harlan P. Moody Larkfield, OK 70000</div>
  </section>

  <section class="card back" aria-label="Business card back, appointment version">
    <div class="brand"><span class="brand-dot"></span>Bright Lens Studio</div>
    <div class="band-appointment">APPOINTMENT ON</div>
    <div class="appointment-fields">
      <div class="field">Time:<span class="field-line"></span></div>
      <div class="field">Date:<span class="field-line"></span></div>
    </div>
  </section>

</body>
</html>
```